Flyer-Design für Organisation von Golf Short Trips
Wir organisieren Golf Short Trips für Golfer aller Altersklassen. Hierfür sind wir auf der Suche nach einem minimalistischem und gleichzeitig hochwertigen Flyer/ Broschüre welches unsere wesentlichen Merkmale verkörpert.
Wir sind ein junges Unternehmen welches sich durch folgende Eigenschaften am besten beschreiben lässt: Innovativ, Disruptiv, Exklusiv, Produktiv, Modern. Diese Unternehmensphilosophie soll durch unseren Flyer erkennbar werden.
We organize golf short trips for golfers of all ages. For this we are looking for a minimalist and at the same time high quality flyer/ broschure which embodies our essential characteristics.
We are a young company which can be best described by the following characteristics: Innovative, Disruptive, Exclusive, Productive, Modern. This corporate philosophy should be recognizable through our flyer.
If possible use:
GRAU: #a2a4aa
GRÜN: #002F01
(SENFGELB: #cfa600)
Format: 138 x 297 / Two Pages (front/back)
So far, we have been working mainly with the Open Sans font.
Underground also Playfair styles. However, we would be happy to receive suggestions from you regarding the fonts.
!!! Please take the text specifications from the attached template: -> flyer_din_a5_hoch_tiefgruen.de.jpeg !!!
The design in general can be created by the designer at his own discretion.
A total of 3 logos must be included in the flyer. That of our company (medium size), the hotel group (small) and the golf course (small).
A small profile picture of the respective trainer should be placed on the front.
All textual content can be accessed via the following link: https://notizwerk-example.net/dokument/7Qx3LmRt9VbWz2KcHnPa5YsEu8JdGfTo4iXkNrBq/edit?usp=sharing

```html
<!DOCTYPE html>
<html lang="de">
<head>
<meta charset="utf-8">
<title>Fairwayhaus – Golf Short Trip</title>
<link rel="stylesheet" href="https://fonts.googleapis.com/css2?family=Open+Sans:wght@300;400;600;700;800&display=swap">
<style>
  :root {
    --green: #173f17;
    --green-deep: #002f01;
    --grey: #a2a4aa;
    --mustard: #cfa600;
    --band: #dcbd45;
    --gold-text: #d4a90f;
    --white: #ffffff;
    --ink: #111111;
  }
  html, body { margin: 0; padding: 0; overflow: hidden; background: var(--white); }
  .flyer {
    position: relative;
    width: 846px;
    height: 1200px;
    overflow: hidden;
    background: var(--white);
    font-family: "Open Sans", sans-serif;
    color: var(--green);
  }
  .brand {
    position: absolute;
    left: 0;
    width: 100%;
    text-align: center;
  }
  .brand-name {
    margin: 0;
    font-weight: 800;
    color: var(--green);
    letter-spacing: 1px;
    line-height: 1;
    white-space: nowrap;
  }
  .brand-tagline {
    margin: 0;
    font-weight: 300;
    color: var(--green);
    line-height: 1;
    white-space: nowrap;
  }
  .brand--top { top: 43px; left: 0; width: 820px; }
  .brand--top .brand-name { font-size: 52px; }
  .brand--top .brand-tagline { font-size: 31px; margin-top: 36px; }
  .brand--bottom { top: 1090px; left: 446px; width: 278px; }
  .brand--bottom .brand-name { font-size: 35px; }
  .brand--bottom .brand-tagline { font-size: 24px; margin-top: 32px; }

  .title-band {
    position: absolute;
    top: 187px;
    left: 0;
    width: 846px;
    height: 78px;
    background: var(--band);
    display: flex;
    align-items: center;
    justify-content: center;
  }
  .title-band h1 {
    margin: 0;
    font-size: 42px;
    font-weight: 700;
    letter-spacing: -2px;
    line-height: 1;
  }
  .title-golf { color: var(--white); }
  .title-short { color: var(--grey); }
  .title-trip { color: var(--green-deep); }

  .course-photo { position: absolute; top: 265px; left: 0; }

  .motto {
    position: absolute;
    left: 630px;
    width: 216px;
    margin: 0;
    padding: 0;
    list-style: none;
  }
  .motto li {
    position: absolute;
    left: 0;
    width: 216px;
    height: 50px;
    padding-left: 50px;
    box-sizing: border-box;
    font-size: 46px;
    line-height: 50px;
    color: var(--ink);
    background: rgba(210, 212, 214, 0.7);
  }
  .motto li:first-child { background: rgba(235, 238, 220, 0.75); }

  .coach-panel { position: absolute; top: 0; left: 0; }
  .coach-photo {
    position: absolute;
    left: 85px;
    top: 810px;
    width: 179px;
    height: 171px;
  }
  .coach {
    position: absolute;
    left: 0;
    top: 1000px;
    width: 337px;
    text-align: center;
    color: var(--green-deep);
  }
  .coach-name { margin: 0; font-size: 37px; font-weight: 400; line-height: 1.1; letter-spacing: 1px; }
  .coach-role { margin: 0; font-size: 23px; line-height: 1.2; letter-spacing: .5px; }
  .coach-quote { margin: 12px 0 0; font-size: 27px; line-height: 34px; }

  .offer {
    position: absolute;
    left: 360px;
    top: 818px;
    width: 470px;
  }
  .offer h2 {
    margin: 0;
    font-size: 39px;
    font-weight: 700;
    color: var(--gold-text);
    line-height: 1.3;
    white-space: nowrap;
  }
  .dates { margin: -4px 0 0; padding: 0; }
  .date-row {
    display: flex;
    align-items: flex-end;
    height: 61px;
  }
  .date-row dt {
    font-size: 28px;
    color: var(--green-deep);
    width: 266px;
    line-height: 1;
    white-space: nowrap;
  }
  .date-row dd {
    margin: 0 0 2px;
    width: 202px;
    height: 0;
    border-bottom: 1.5px solid var(--green-deep);
  }
</style>
</head>
<body>
<main class="flyer">
  <header class="brand brand--top">
    <p class="brand-name">FAIRWAYHAUS</p>
    <p class="brand-tagline">„Eine Klasse für sich“</p>
  </header>

  <div class="title-band">
    <h1><span class="title-golf">GOLF</span> <span class="title-short">SHORT</span> <span class="title-trip">TRIP</span></h1>
  </div>

  <svg class="course-photo" width="846" height="565" viewBox="0 0 846 565" role="img" aria-label="Foto eines Golfplatzes im Morgennebel mit Bunkern und Bäumen, Country Club Arvenhain">
    <defs>
      <linearGradient id="courseTone" x1="0" y1="0" x2="0" y2="1">
        <stop offset="0" stop-color="#e4ebee"/>
        <stop offset="0.2" stop-color="#c7d0c4"/>
        <stop offset="0.38" stop-color="#5f8a3a"/>
        <stop offset="0.6" stop-color="#b89a6a"/>
        <stop offset="0.78" stop-color="#6b8b3c"/>
        <stop offset="1" stop-color="#2f5a1c"/>
      </linearGradient>
    </defs>
    <polygon points="0,0 846,0 846,496 0,564" fill="url(#courseTone)"/>
  </svg>

  <ul class="motto">
    <li style="top:413px">PLAY</li>
    <li style="top:481px">RELAX</li>
    <li style="top:550px">STAY</li>
  </ul>

  <svg class="coach-panel" width="337" height="1200" viewBox="0 0 337 1200" aria-hidden="true">
    <polygon points="0,829 337,800 337,1200 0,1200" fill="var(--grey)"/>
  </svg>
  <svg class="coach-photo" width="179" height="171" viewBox="0 0 179 171" role="img" aria-label="Porträtfoto des Golftrainers Lukas Brenner">
    <defs>
      <linearGradient id="coachTone" x1="0" y1="0" x2="0" y2="1">
        <stop offset="0" stop-color="#eef0ee"/>
        <stop offset="0.55" stop-color="#b79a86"/>
        <stop offset="1" stop-color="#4cc33c"/>
      </linearGradient>
    </defs>
    <rect width="179" height="171" fill="url(#coachTone)"/>
  </svg>

  <section class="coach">
    <h3 class="coach-name">Lukas Brenner</h3>
    <p class="coach-role">Golf Professionell</p>
    <p class="coach-quote">„Golferlebnisse<br>die neue Maßstäbe<br>setzen!“</p>
  </section>

  <section class="offer">
    <h2>10% FÜR EARLY BIRDS</h2>
    <dl class="dates">
      <div class="date-row"><dt>Erster Zeitraum:</dt><dd></dd></div>
      <div class="date-row"><dt>Zweiter Zeitraum:</dt><dd></dd></div>
      <div class="date-row"><dt>Early Bird bis:</dt><dd></dd></div>
    </dl>
  </section>

  <footer class="brand brand--bottom">
    <p class="brand-name">FAIRWAYHAUS</p>
    <p class="brand-tagline">„Eine Klasse für sich“</p>
  </footer>
</main>
</body>
</html>
```